Maplerise Trading Inc. needs an innovative idea for letterhead and visiting cards.

Maplerise Trading Inc. is a Canadian brand since 2007. It is a renown dealer of kids and office furniture locally. Moreover, exporting electric fixtures e.g. switches, LED's, down-lights etc. to Middle East and Africa. We have initiated a number of steps including re-branding, to boost our export in 2020. We have successfully designed our new logo a few months ago through 'Artfolio' and now we are looking for an innovative idea for a letterhead.
Some key points:
• Red, black and white are the three colors used in all our packaging and furniture. (grey is optional)
• Shouldn’t be too wide.
• Use of watermark is preferable.
• You can visit our North American site at www.mapleriseinc.com. Export website of the company will be launched soon. www.mapleriseinc.ca
• Same letterhead will be used locally and internationally.
• Our new logo and sample packaging is attached.

```html
<!DOCTYPE html>
<html lang="en">
<head>
<meta charset="utf-8">
<title>Maplerise Trading Inc. – Letterhead</title>
<link rel="stylesheet" href="https://fonts.googleapis.com/css2?family=Arimo:wght@400;700&family=Archivo+Black&display=swap">
<style>
  :root {
    --backdrop: #2e2e2e;
    --paper: #ffffff;
    --brand-red: #a4232a;
    --ink: #1b1b1b;
    --ink-grey: #555555;
  }
  * { box-sizing: border-box; margin: 0; padding: 0; }
  html, body {
    width: 1200px;
    height: 780px;
    overflow: hidden;
    background: var(--backdrop);
    font-family: "Arimo", Arial, sans-serif;
  }
  .canvas {
    width: 1200px;
    height: 780px;
    display: flex;
    align-items: center;
    justify-content: center;
  }
  .letterhead {
    position: relative;
    width: 524px;
    height: 740px;
    background: var(--paper);
    overflow: hidden;
    color: var(--ink);
  }

  /* Brand block */
  .brand {
    position: absolute;
    left: 38px;
    top: 46px;
    display: flex;
    align-items: center;
    gap: 12px;
  }
  .brand-square {
    width: 46px;
    height: 46px;
    background: var(--brand-red);
    border-radius: 6px;
  }
  .brand-name {
    font-family: "Arimo", Arial, sans-serif;
    font-weight: 400;
    font-size: 24px;
    line-height: 1.02;
    letter-spacing: 1px;
    text-transform: uppercase;
    color: var(--ink-grey);
  }

  /* Divider */
  .divider {
    position: absolute;
    left: 176px;
    top: 150px;
    width: 2px;
    height: 470px;
    background: var(--brand-red);
  }

  /* Contact column */
  .contact {
    position: absolute;
    left: 30px;
    top: 300px;
    width: 136px;
    list-style: none;
    display: flex;
    flex-direction: column;
    gap: 12px;
  }
  .contact-item {
    display: flex;
    align-items: flex-start;
    gap: 7px;
    font-size: 8.4px;
    line-height: 1.3;
    color: var(--ink);
  }
  .contact-icon {
    flex: 0 0 16px;
    width: 16px;
    height: 16px;
  }

  /* Letter body */
  .letter {
    position: absolute;
    left: 194px;
    top: 146px;
    width: 296px;
  }
  .headline {
    font-family: "Archivo Black", "Arial Black", sans-serif;
    font-size: 33px;
    line-height: 1;
    letter-spacing: 0.5px;
    color: var(--brand-red);
    margin-bottom: 12px;
  }
  .salutation,
  .letter p {
    font-size: 7.6px;
    line-height: 1.38;
    color: var(--ink);
  }
  .salutation { margin-bottom: 7px; }
  .letter p + p { margin-top: 9px; }
  .closing { margin-top: 11px; font-size: 7.6px; }

  /* Footer band */
  .footer-band {
    position: absolute;
    left: 0;
    right: 0;
    bottom: 0;
    height: 46px;
    background: var(--brand-red);
  }
</style>
</head>
<body>
<main class="canvas">
  <article class="letterhead">

    <header class="brand">
      <div class="brand-square"></div>
      <div class="brand-name">Maplerise<br>Trading</div>
    </header>

    <div class="divider"></div>

    <ul class="contact">
      <li class="contact-item">
        <svg class="contact-icon" viewBox="0 0 16 16" aria-hidden="true">
          <circle cx="8" cy="8" r="8" fill="var(--brand-red)"/>
          <path d="M8 3.6a2.8 2.8 0 0 0-2.8 2.8c0 2.1 2.8 5.4 2.8 5.4s2.8-3.3 2.8-5.4A2.8 2.8 0 0 0 8 3.6zm0 3.9a1.1 1.1 0 1 1 0-2.2 1.1 1.1 0 0 1 0 2.2z" fill="#fff"/>
        </svg>
        <span>48 Birchmount Rd. Unit 210,<br>Markham,<br>ON L3R 2K7.</span>
      </li>
      <li class="contact-item">
        <svg class="contact-icon" viewBox="0 0 16 16" aria-hidden="true">
          <circle cx="8" cy="8" r="8" fill="var(--brand-red)"/>
          <path d="M5.6 4.2l1.3-.2.8 1.9-.9.7c.4.9 1.1 1.6 2 2l.7-.9 1.9.8-.2 1.3c-.1.4-.5.7-.9.7C7.6 10.4 5.2 8 5 5.1c0-.4.3-.8.6-.9z" fill="#fff"/>
        </svg>
        <span>+1 (888) 555-0142.</span>
      </li>
      <li class="contact-item">
        <svg class="contact-icon" viewBox="0 0 16 16" aria-hidden="true">
          <circle cx="8" cy="8" r="8" fill="var(--brand-red)"/>
          <rect x="4" y="5.2" width="8" height="5.6" rx="0.6" fill="#fff"/>
          <path d="M4.3 5.5L8 8.4l3.7-2.9" fill="none" stroke="var(--brand-red)" stroke-width="0.8"/>
        </svg>
        <span>www.mapleriseinc.com<br>www.mapleriseinc.ca</span>
      </li>
    </ul>

    <section class="letter">
      <h1 class="headline">HEADLINE</h1>
      <div class="salutation">Dear Sir,</div>
      <p>Lorem Ipsum is simply dummy text of the printing and typesetting industry. Lorem Ipsum has been the industry's standard dummy text ever since the 1500s, when an unknown printer took a galley of type and scrambled it to make a type specimen book. It has survived not only five centuries, but also the leap into electronic typesetting, remaining essentially unchanged. It was popularised in the 1960s with the release of Typeleaf sheets containing Lorem Ipsum passages, and more recently with desktop publishing software like Pagewright Studio including versions of Lorem Ipsum.</p>
      <p>It is a long established fact that a reader will be distracted by the readable content of a page when looking at its layout. The point of using Lorem Ipsum is that it has a more-or-less normal distribution of letters, as opposed to using 'Content here, content here', making it look like readable English. Many desktop publishing packages and web page editors now use Lorem Ipsum as their default model text, and a search for 'lorem ipsum' will uncover many web sites still in their infancy. Various versions have evolved over the years, sometimes by accident, sometimes on purpose (injected humour and the like).</p>
      <p>Contrary to popular belief, Lorem Ipsum is not simply random text. It has roots in a piece of classical Latin literature from 45 BC, making it over 2000 years old. A Latin professor looked up one of the more obscure Latin words, consectetur, from a Lorem Ipsum passage, and going through the cites of the word in classical literature, discovered the undoubtable source. Lorem Ipsum comes from sections 1.10.32 and 1.10.33 of "de Rebus Honestis" (On Honest Matters) by Marcus Varenus, written in 45 BC. This book is a treatise on the theory of ethics, very popular during the Renaissance. The first line of Lorem Ipsum, "Lorem ipsum dolor sit amet..", comes from a line in section 1.10.32</p>
      <div class="closing">Thank you</div>
    </section>

    <div class="footer-band"></div>
  </article>
</main>
</body>
</html>
```